Beach Polo Event Flyer

The project consists of a flyer for a beach polo event that will occur on August 30 and 31

The flyer should contain the event details in spanish:
IV MARENQUA SHORE RIDING CUP
Hotel Varlowe
Agosto 30 y 31 2014
Horario: 2pm a 6pm
(Varlowe Logo)

Also contact info below:
info@brisadelvarclub.example
www.brisadelvarclub.example

A Space should be left on the bottom for us to add the sponsor logos when we have them.

The general idea is to do a flyer that looks elegant, inviting, inspired on the beach and the caribbean and shows the beauty of the sport and the beach.

I am attaching the flyer that a friend made that we DO NOT LIKE and some flyers from events in other parts of the world that we do like.
Also attached you will find the BRISADEL VAR CLUB logo which should go somewhere in the flyer. We are also attaching pictures from the past event in case you would need to use them.
We are open for any questions

```html
<!DOCTYPE html>
<html lang="es">
<head>
<meta charset="utf-8">
<title>IV Marenqua Shore Riding Cup</title>
<link href="https://fonts.googleapis.com/css2?family=Libre+Bodoni:wght@400;700&display=swap" rel="stylesheet">
<style>
  :root {
    --sky-top: #6b95b4;
    --sky-low: #7ea5c0;
    --sea: #8fa9a8;
    --surf: #d9dcd6;
    --sand: #c8b594;
    --sand-deep: #b9a27c;
    --ink-light: #ffffff;
    --band: #2e2725;
    --paper: #ffffff;
  }
  * { margin: 0; padding: 0; box-sizing: border-box; }
  html, body { width: 849px; height: 1200px; overflow: hidden; background: var(--paper); }
  .flyer {
    position: relative;
    width: 849px;
    height: 1200px;
    background: var(--paper);
    font-family: "Libre Bodoni", "Bodoni Moda", serif;
    color: var(--ink-light);
  }
  .event-scene {
    position: absolute;
    left: 0; top: 0;
    width: 849px; height: 1012px;
    background: linear-gradient(180deg,
      var(--sky-top) 0%,
      var(--sky-low) 62%,
      var(--sea) 65%,
      var(--sea) 70%,
      var(--surf) 74%,
      var(--sand) 78%,
      var(--sand-deep) 100%);
  }
  .divider-band {
    position: absolute;
    left: 0; top: 1012px;
    width: 849px; height: 15px;
    background: var(--band);
  }
  .sponsor-space {
    position: absolute;
    left: 0; top: 1027px;
    width: 849px; height: 173px;
    background: var(--paper);
  }
  .club-mark {
    position: absolute;
    left: 0; top: 40px;
    width: 849px;
    text-align: center;
  }
  .club-mark svg { display: block; margin: 0 auto; }
  .club-name {
    margin-top: 20px;
    font-weight: 400;
    font-size: 27px;
    letter-spacing: 2px;
    line-height: 30px;
  }
  .event-title {
    position: absolute;
    left: 0; top: 322px;
    width: 849px;
    text-align: center;
    font-weight: 700;
    font-size: 60px;
    line-height: 80px;
    letter-spacing: 1px;
  }
  .venue {
    position: absolute;
    left: 0; top: 786px;
    width: 849px;
    text-align: center;
  }
  .venue svg { display: block; margin: 0 auto; }
  .venue-name {
    font-weight: 700;
    font-size: 42px;
    line-height: 46px;
    margin-top: 4px;
  }
  .venue-details {
    font-weight: 400;
    font-size: 17px;
    line-height: 22px;
    margin-top: 4px;
  }
  .contact {
    position: absolute;
    left: 0; top: 955px;
    width: 849px;
    text-align: center;
    font-size: 17px;
    line-height: 22px;
  }
</style>
</head>
<body>
<main class="flyer">
  <div class="event-scene" role="img" aria-label="Photo of three polo players on horseback riding across a sunny beach with the sea and blue sky behind"></div>

  <header class="club-mark">
    <svg width="100" height="100" viewBox="0 0 100 100" aria-hidden="true">
      <circle cx="50" cy="50" r="46" fill="none" stroke="var(--ink-light)" stroke-width="3"/>
    </svg>
    <p class="club-name">BRISADEL VAR CLUB</p>
  </header>

  <h1 class="event-title">IV MARENQUA<br>SHORE RIDING CUP</h1>

  <section class="venue">
    <svg width="36" height="36" viewBox="0 0 36 36" aria-hidden="true">
      <circle cx="18" cy="18" r="16" fill="none" stroke="var(--ink-light)" stroke-width="3"/>
    </svg>
    <p class="venue-name">Varlowe</p>
    <p class="venue-details">Hotel Varlowe<br>Agosto 30 y 31 2014 &nbsp;|&nbsp; Horario: 2pm a 6pm</p>
  </section>

  <p class="contact">info@brisadelvarclub.example &nbsp;|&nbsp; www.brisadelvarclub.example</p>

  <div class="divider-band"></div>
  <footer class="sponsor-space" aria-label="Espacio para patrocinadores"></footer>
</main>
</body>
</html>
```